Hi. I need a banner ad designed for our real estate CRM. The website is www.quellaestate.com.au and the ad will be used to send people to the website. See the website for the style of our design/branding

It needs to have our logo and then have the words 'Australia's most cost effective real estate CRM' and also 'no hidden fees, no lock in contracts'. It also needs to have a button that says 'start your free 14 day trial now'

The banner needs to be 600 x 90 pixels

```html
<!DOCTYPE html>
<html lang="en">
<head>
<meta charset="utf-8">
<title>Quella Estate – Real Estate CRM Banner</title>
<link rel="stylesheet" href="https://fonts.googleapis.com/css2?family=Montserrat:wght@400;500;700&display=swap">
<style>
  :root {
    --page-bg: #dedede;
    --ink-dark: #252525;
    --chevron-grey: #e2e2e2;
    --brand-red: #cc0a26;
    --deep-red: #ad0220;
    --bright-red: #e02336;
    --white: #ffffff;
  }
  * { margin: 0; padding: 0; box-sizing: border-box; }
  html, body {
    width: 1200px; height: 974px; overflow: hidden;
    background: var(--page-bg);
    font-family: "Montserrat", Arial, sans-serif;
  }
  .stage { position: relative; width: 1200px; height: 974px; }
  .banner {
    position: absolute; left: 58px; top: 256px;
    width: 1083px; height: 435px;
  }
  .banner-art { position: absolute; inset: 0; width: 100%; height: 100%; display: block; }
  .headline {
    position: absolute; left: 48px; top: 72px;
    color: var(--white); font-weight: 700;
    font-size: 32px; line-height: 38px; letter-spacing: 0.5px;
    text-transform: uppercase; white-space: nowrap;
  }
  .subline {
    position: absolute; left: 48px; top: 159px;
    color: var(--white); font-weight: 500;
    font-size: 23px; line-height: 28px; letter-spacing: 5.6px;
    text-transform: uppercase; white-space: nowrap;
  }
  .cta {
    position: absolute; left: 48px; top: 262px;
    width: 245px; height: 50px;
    background: var(--brand-red); color: var(--white);
    display: flex; align-items: center; justify-content: center;
    text-align: center; text-decoration: none;
    font-weight: 700; font-size: 17px; line-height: 20px; letter-spacing: 3.4px;
    text-transform: uppercase;
  }
  .web-link {
    position: absolute; left: 48px; top: 355px;
    display: flex; align-items: center; gap: 6px;
    color: var(--white); font-size: 10.5px; font-weight: 500;
    text-decoration: none;
  }
  .web-link svg { width: 17px; height: 17px; }
  .brand {
    position: absolute; left: 566px; top: 41px;
    display: flex; align-items: center; gap: 6px;
    color: var(--white); font-size: 15px; font-weight: 400; letter-spacing: 1.2px;
  }
  .brand-dot { width: 10px; height: 10px; border-radius: 50%; background: var(--white); }
</style>
</head>
<body>
<main class="stage">
  <section class="banner">
    <svg class="banner-art" viewBox="0 0 1931 776" preserveAspectRatio="none" aria-hidden="false">
      <defs>
        <linearGradient id="photo-tone" x1="0" y1="0" x2="0.3" y2="1">
          <stop offset="0" stop-color="#b9b3ad"/>
          <stop offset="0.4" stop-color="#8d8580"/>
          <stop offset="0.65" stop-color="#a3673a"/>
          <stop offset="1" stop-color="#7c4f2a"/>
        </linearGradient>
      </defs>
      <rect class="panel-dark" width="1931" height="776" fill="var(--ink-dark)"/>
      <g role="img" aria-label="Photo of a small model house with red walls and a grey roof, house keys on a wooden table in front">
        <polygon points="1662,0 1931,0 1931,776 1204,776 1056,622" fill="url(#photo-tone)"/>
      </g>
      <polygon class="red-field" points="884,0 1662,0 1056,622 1204,776 680,776 1152,292" fill="var(--brand-red)"/>
      <polygon class="deep-stripe" points="1436,0 1546,0 784,776 680,776 1152,292" fill="var(--deep-red)"/>
      <polygon class="bright-stripe" points="1546,0 1662,0 1056,622 900,776 784,776" fill="var(--bright-red)"/>
      <polygon class="chevron-edge" points="858,0 884,0 1152,292 680,776 654,776 1126,292" fill="var(--chevron-grey)"/>
    </svg>

    <div class="brand"><span class="brand-dot"></span>QUELLAESTATE</div>

    <h1 class="headline">Australia's most cost<br>effective real estate CRM</h1>
    <p class="subline">No hidden fees,<br>no lock in contracts</p>

    <a class="cta" href="#">Start your free<br>14 day trial now</a>

    <a class="web-link" href="#">
      <svg viewBox="0 0 20 20" fill="none" stroke="#ffffff" stroke-width="1">
        <circle cx="10" cy="10" r="9"/>
        <ellipse cx="10" cy="10" rx="4" ry="9"/>
        <line x1="1" y1="10" x2="19" y2="10"/>
        <line x1="2.5" y1="5.5" x2="17.5" y2="5.5"/>
        <line x1="2.5" y1="14.5" x2="17.5" y2="14.5"/>
        <line x1="10" y1="1" x2="10" y2="19"/>
      </svg>
      www.quellaestate.com.au
    </a>
  </section>
</main>
</body>
</html>
```